Business Card and Stationary for a Non Profit Educational Organization supporting Immigrants
ΣΩΜΑΤΕΙΟ ΠΟΛΙΤΙΣΤΙΚΗΣ ΓΕΦΥΡΑΣ ΦΙΛΩΝ
Business Card and Stationary  for a Non Profit Educational Organization supporting Immigrants - Education
Creative Brief
Professional
Ardit Merkaj
Αντιπρόεδρος του Δ.Σ
ΚΑΛΥΨΟΥΣ 42, (ΟΡΟΦΟΣ 2ος ) ΑΘΗΝΑ T.K. 117 81
Τηλ.: 210 6148072
info@sopog-mail.gr
www.sopog-mail.gr
The card will be double sided, one part in Greek Language (just take the text copy/paste) and the other side identical in Albanian (the only difference here is that we will add another icon and coresponding text "Qendra Mësimore Ylli I Mëngjesit")
SHOQATA PËR URËN KULTURORE TË MIQVE Qendra Mësimore Ylli I Mëngjesit Ardit Merkaj Nënkryetar Rruga Kalipso Nr. 42 (Kati 2-të) Athinë 11781, Greqi +30 210 6148072 +30 6945028316 info@sopog-mail.gr www.sopog-mail.gr

```html
<!DOCTYPE html>
<html lang="el">
<head>
<meta charset="UTF-8">
<title>ΣΩΜΑΤΕΙΟ ΠΟΛΙΤΙΣΤΙΚΗΣ ΓΕΦΥΡΑΣ ΦΙΛΩΝ – Business Card</title>
<link href="https://fonts.googleapis.com/css2?family=Open+Sans:wght@400;600;700&display=swap" rel="stylesheet">
<style>
  :root {
    --navy: #27305f;
    --red: #d2232e;
    --ink: #3a3a3a;
    --icon: #4a4a4a;
    --paper: #ffffff;
    --backdrop: #e9e9ea;
  }
  * { margin: 0; padding: 0; box-sizing: border-box; }
  html, body {
    width: 1200px; height: 901px; overflow: hidden;
    background: var(--backdrop);
    font-family: "Open Sans", Arial, sans-serif;
  }
  .card {
    position: absolute; left: 100px; top: 165px;
    width: 1000px; height: 571px;
    background: var(--paper);
    overflow: hidden;
    box-shadow: 0 10px 30px rgba(0,0,0,0.12);
  }
  .side-band {
    position: absolute; top: 0; right: 0; bottom: 0; width: 92px;
    background: var(--navy);
  }
  .side-band::before {
    content: ""; position: absolute; top: 0; bottom: 0; left: -22px; width: 22px;
    background: repeating-linear-gradient(180deg, var(--red) 0 14px, #fff 14px 22px);
    opacity: 0.9;
  }
  .side-band .web {
    position: absolute; left: 50%; top: 50%;
    transform: translate(-50%, -50%) rotate(90deg);
    color: #fff; font-weight: 700; font-size: 26px; letter-spacing: 5px;
    white-space: nowrap;
  }
  .base-line {
    position: absolute; left: 0; right: 114px; bottom: 0; height: 12px;
    background: var(--navy);
  }
  .base-line::before {
    content: ""; position: absolute; left: 0; right: 0; top: -6px; height: 4px;
    background: var(--red);
  }
  .brand {
    position: absolute; left: 70px; top: 70px;
    display: flex; align-items: center; gap: 14px;
  }
  .brand-dot { width: 44px; height: 44px; border-radius: 50%; background: var(--red); }
  .brand-name {
    font-size: 50px; font-weight: 700; color: var(--navy); letter-spacing: 1px; line-height: 1;
  }
  .brand-tagline {
    position: absolute; left: 72px; top: 132px;
    font-size: 9px; font-weight: 600; color: var(--navy); letter-spacing: 0.3px;
  }
  .person {
    position: absolute; left: 50px; top: 335px;
    padding-left: 24px;
  }
  .person::before {
    content: ""; position: absolute; left: 0; top: 26px;
    border-left: 16px solid var(--red);
    border-top: 13px solid transparent; border-bottom: 13px solid transparent;
  }
  .person-name { font-size: 36px; font-weight: 600; color: var(--navy); line-height: 1.2; }
  .person-role { font-size: 30px; color: var(--ink); line-height: 1.25; }
  .contacts {
    position: absolute; left: 540px; top: 220px;
    list-style: none; font-size: 18px; color: var(--ink);
  }
  .contacts li { display: flex; align-items: flex-start; gap: 12px; margin-bottom: 8px; line-height: 1.35; }
  .contacts svg { flex: 0 0 22px; width: 22px; height: 22px; margin-top: 1px; }
</style>
</head>
<body>
  <main class="card">
    <div class="brand">
      <span class="brand-dot"></span>
      <span class="brand-name">SOPOG</span>
    </div>
    <p class="brand-tagline">ΣΩΜΑΤΕΙΟ ΠΟΛΙΤΙΣΤΙΚΗΣ ΓΕΦΥΡΑΣ ΦΙΛΩΝ</p>

    <section class="person">
      <h1 class="person-name">Ardit Merkaj</h1>
      <p class="person-role">Αντιπρόεδρος του Δ.Σ</p>
    </section>

    <ul class="contacts">
      <li>
        <svg viewBox="0 0 22 22"><circle cx="11" cy="11" r="11" fill="var(--icon)"/><path d="M11 5a4 4 0 0 0-4 4c0 3 4 8 4 8s4-5 4-8a4 4 0 0 0-4-4zm0 5.5a1.5 1.5 0 1 1 0-3 1.5 1.5 0 0 1 0 3z" fill="#fff"/></svg>
        <span>ΚΑΛΥΨΟΥΣ 42, (ΟΡΟΦΟΣ 2ος )<br>ΑΘΗΝΑ T.K. 117 81</span>
      </li>
      <li>
        <svg viewBox="0 0 22 22"><circle cx="11" cy="11" r="11" fill="var(--icon)"/><path d="M8 6l2 3-1.2 1.2c.7 1.4 1.6 2.3 3 3L13 12l3 2-1 2c-4 0-8-4-8-8z" fill="#fff"/></svg>
        <span>Τηλ.: 210 6148072</span>
      </li>
      <li>
        <svg viewBox="0 0 22 22"><circle cx="11" cy="11" r="11" fill="var(--icon)"/><rect x="8" y="5" width="6" height="12" rx="1" fill="#fff"/><rect x="9" y="6.5" width="4" height="7" fill="var(--icon)"/></svg>
        <span>+30 6945028316</span>
      </li>
      <li>
        <svg viewBox="0 0 22 22"><circle cx="11" cy="11" r="11" fill="var(--icon)"/><rect x="5.5" y="7" width="11" height="8" rx="1" fill="#fff"/><path d="M5.5 7.5l5.5 4 5.5-4" fill="none" stroke="var(--icon)" stroke-width="1.2"/></svg>
        <span>info@sopog-mail.gr</span>
      </li>
      <li>
        <svg viewBox="0 0 22 22"><circle cx="11" cy="11" r="11" fill="var(--icon)"/><circle cx="11" cy="11" r="5.5" fill="none" stroke="#fff" stroke-width="1.2"/><ellipse cx="11" cy="11" rx="2.3" ry="5.5" fill="none" stroke="#fff" stroke-width="1.1"/><path d="M5.5 11h11" stroke="#fff" stroke-width="1.1"/></svg>
        <span>www.sopog-mail.gr</span>
      </li>
    </ul>

    <div class="base-line"></div>
    <aside class="side-band"><span class="web">www.sopog-mail.gr</span></aside>
  </main>
</body>
</html>
```